Business Card Design Project

Corwen Property Management

Our Business is residential property management, we therefore need a card that displays a professional image, but is clear and concise, and easy to read
Updates

We are committed now guys and girls, loving what we are seeing so far! 

Target Market(s)

Landlords, Rental Property Owners

Industry/Entity Type

Residential

Requirements
Must have
• Dean Fosterly - Principal
Tessa Fosterly - Director (Property Management)

PO Box 718
Holloway SA 5093

Dean: 0419 372 508
Tessa: 0419 613 947

www.corwenpropertymanagement.com.au
admin@corwenpropertymanagement.com.au

Nice to have
• I would like the card to be double sided, white background on the information side and then colour on the reverse, in blue or black and incorporating our logo

```html
<!DOCTYPE html>
<html lang="en">
<head>
<meta charset="utf-8">
<title>Corwen Property Management – Business Cards</title>
<link rel="stylesheet" href="https://fonts.googleapis.com/css2?family=Open+Sans:wght@400;600&display=swap">
<style>
  :root {
    --backdrop: #d8c28c;
    --card: #121212;
    --card-edge: #1c1c1c;
    --brand-blue: #1a8fef;
    --text-light: #ffffff;
    --text-soft: #dcdcdc;
    --text-dim: #a8a8a8;
  }
  * { margin: 0; padding: 0; box-sizing: border-box; }
  html, body {
    width: 1200px;
    height: 900px;
    overflow: hidden;
    background: var(--backdrop);
    font-family: "Open Sans", Arial, sans-serif;
  }
  .canvas {
    position: relative;
    width: 1200px;
    height: 900px;
  }
  .card {
    position: absolute;
    background: var(--card);
    border: 1px solid var(--card-edge);
    border-radius: 12px;
  }
  .card--front {
    left: 140px; top: 62px;
    width: 717px; height: 420px;
    z-index: 2;
    box-shadow: 0 6px 14px rgba(0,0,0,0.35);
  }
  .card--back {
    left: 333px; top: 420px;
    width: 770px; height: 450px;
    z-index: 1;
    box-shadow: 0 6px 14px rgba(0,0,0,0.35);
  }
  .brand {
    position: absolute;
    display: flex;
    align-items: center;
    gap: 18px;
    color: var(--text-light);
  }
  .brand__mark {
    background: var(--brand-blue);
    flex: none;
  }
  .brand__name {
    display: flex;
    flex-direction: column;
    line-height: 1;
  }
  .brand__title { font-weight: 600; letter-spacing: -1px; }
  .brand__tagline { font-weight: 400; }
  .card--front .brand { left: 135px; top: 168px; }
  .card--front .brand__mark { width: 80px; height: 80px; }
  .card--front .brand__title { font-size: 84px; }
  .card--front .brand__tagline { font-size: 19px; margin-top: 6px; padding-left: 4px; }
  .card--back .brand { left: 45px; top: 168px; }
  .card--back .brand__mark { width: 64px; height: 64px; }
  .card--back .brand__title { font-size: 66px; }
  .card--back .brand__tagline { font-size: 15px; margin-top: 5px; padding-left: 3px; }
  .divider {
    position: absolute;
    left: 411px; top: 140px;
    width: 2px; height: 172px;
    background: var(--brand-blue);
  }
  .contact {
    position: absolute;
    left: 431px; top: 96px;
    list-style: none;
    color: var(--text-soft);
    font-size: 14.2px;
    letter-spacing: 0;
    line-height: 30.7px;
  }
  .contact li { height: 30.7px; white-space: nowrap; }
  .contact__note { font-size: 8.5px; color: var(--text-dim); }
</style>
</head>
<body>
<main class="canvas">
  <section class="card card--back" aria-label="Card information side">
    <div class="brand">
      <span class="brand__mark"></span>
      <span class="brand__name">
        <span class="brand__title">Corwen</span>
        <span class="brand__tagline">Property Management</span>
      </span>
    </div>
    <span class="divider"></span>
    <ul class="contact">
      <li>Dean Fosterly - Principal</li>
      <li>Tessa Fosterly - Director <span class="contact__note">(Property Management)</span></li>
      <li>PO Box 718</li>
      <li>Holloway SA 5093</li>
      <li>Dean: 0419 372 508</li>
      <li>Tessa: 0419 613 947</li>
      <li>www.corwenpropertymanagement.com.au</li>
      <li>admin@corwenpropertymanagement.com.au</li>
    </ul>
  </section>

  <section class="card card--front" aria-label="Card brand side">
    <div class="brand">
      <span class="brand__mark"></span>
      <span class="brand__name">
        <span class="brand__title">Corwen</span>
        <span class="brand__tagline">Property Management</span>
      </span>
    </div>
  </section>
</main>
</body>
</html>
```